Letter head / email signature/ contract document templates

We need a professional email signature and letterhead designed for our established carpentry and maintenance company. Our Logo (attached) was originally designed 6 years ago by design guru and we love it, looking for something to compliment it ( not a home job)

```html
<!DOCTYPE html>
<html lang="en">
<head>
<meta charset="utf-8">
<title>Kestrel Home Care – Stationery</title>
<link href="https://fonts.googleapis.com/css2?family=Lato:wght@400;700;900&family=Arimo:wght@400&display=swap" rel="stylesheet">
<style>
  :root {
    --backdrop: #8b8b8d;
    --paper: #f1f1f2;
    --red: #d40000;
    --ink: #3a3a3c;
    --ink-soft: #555558;
    --roller: #9a9a9c;
    --roller-dark: #5c5c5e;
  }
  * { box-sizing: border-box; margin: 0; padding: 0; }
  html, body { width: 1200px; height: 858px; overflow: hidden; }
  body {
    background: var(--backdrop);
    font-family: "Lato", sans-serif;
    color: var(--ink);
    position: relative;
  }
  .sheet { position: absolute; background: var(--paper); }

  .brand { display: flex; align-items: center; gap: 5px; color: var(--ink); font-family: "Lato", sans-serif; font-weight: 900; white-space: nowrap; letter-spacing: -0.2px; }
  .brand-square { background: var(--red); flex: none; }

  .contact { font-family: "Lato", sans-serif; color: var(--ink-soft); line-height: 1.3; }
  .contact-row { display: flex; align-items: center; gap: 5px; }
  .icon { flex: none; fill: var(--red); }
  .icon-outline { fill: none; stroke: var(--ink); }

  .roller-art { position: absolute; background: linear-gradient(90deg, var(--roller), var(--roller-dark)); border-radius: 2px; }

  /* Letterhead */
  .letterhead { left: 122px; top: 65px; width: 507px; height: 713px; }
  .letterhead .brand { position: absolute; left: 35px; top: 75px; font-size: 20px; }
  .letterhead .brand-square { width: 10px; height: 10px; }
  .letterhead .contact { position: absolute; left: 360px; top: 57px; font-size: 7px; }
  .letterhead .contact .gap { height: 8px; }
  .letter-body { position: absolute; left: 38px; top: 176px; width: 432px; font-family: "Arimo", sans-serif; color: var(--ink-soft); }
  .greeting { font-size: 12px; margin-bottom: 20px; color: var(--ink); }
  .letter-body p { font-size: 7.2px; line-height: 1.5; text-align: justify; margin-bottom: 10px; }
  .closing { font-size: 7.2px; margin-top: 16px; }
  .signature-art { width: 146px; height: 38px; margin-top: 18px; background: linear-gradient(90deg, #e4e4e6, #d8d8da); border-radius: 3px; }
  .letterhead .band { position: absolute; left: 0; top: 667px; width: 450px; height: 21px; background: var(--red); color: #fff; font-size: 8.5px; letter-spacing: 2px; display: flex; align-items: center; justify-content: center; padding-left: 40px; }
  .letterhead .roller-art { left: 444px; top: 656px; width: 48px; height: 42px; }

  /* Business card */
  .card { left: 663px; top: 206px; width: 184px; height: 279px; }
  .card .brand { position: absolute; left: 22px; top: 52px; font-size: 15px; }
  .card .brand-square { width: 8px; height: 8px; }
  .card .person { position: absolute; left: 22px; top: 134px; }
  .card .name { color: var(--red); font-weight: 700; font-size: 13px; }
  .card .role { font-size: 9px; color: var(--ink); }
  .card .contact { position: absolute; left: 22px; top: 176px; font-size: 9px; line-height: 1.25; }
  .card .contact .gap { height: 4px; }
  .card .band { position: absolute; left: 0; top: 255px; width: 148px; height: 14px; background: var(--red); color: #fff; font-size: 8.5px; padding-left: 21px; display: flex; align-items: center; }
  .card .roller-art { left: 146px; top: 247px; width: 30px; height: 28px; }

  /* Email signature, wide */
  .sig-wide { left: 663px; top: 510px; width: 477px; height: 147px; }
  .sig-wide .brand { position: absolute; left: 82px; top: 63px; font-size: 16px; }
  .sig-wide .brand-square { width: 8px; height: 8px; }
  .sig-wide .divider { position: absolute; left: 239px; top: 36px; width: 1px; height: 74px; background: #cfcfd1; }
  .sig-wide .contact { position: absolute; left: 260px; top: 39px; font-size: 9px; line-height: 1.25; }
  .sig-wide .contact .gap { height: 4px; }
  .sig-wide .band { position: absolute; left: 0; top: 124px; width: 436px; height: 10px; background: var(--red); }
  .sig-wide .roller-art { left: 434px; top: 116px; width: 26px; height: 20px; }

  /* Email signature, compact */
  .sig-compact { left: 662px; top: 680px; width: 477px; height: 92px; }
  .sig-compact .brand { position: absolute; left: 24px; top: 34px; font-size: 12px; }
  .sig-compact .brand-square { width: 7px; height: 7px; }
  .sig-compact .divider { position: absolute; top: 24px; width: 1px; height: 38px; background: #cfcfd1; }
  .sig-compact .divider.one { left: 145px; }
  .sig-compact .divider.two { left: 314px; }
  .sig-compact .contact { position: absolute; font-size: 9px; line-height: 1.25; }
  .sig-compact .contact.phones { left: 161px; top: 29px; }
  .sig-compact .contact.address { left: 329px; top: 31px; }
  .sig-compact .band { position: absolute; left: 0; top: 75px; width: 434px; height: 9px; background: var(--red); }
  .sig-compact .roller-art { left: 433px; top: 70px; width: 20px; height: 16px; }
</style>
</head>
<body>

<svg width="0" height="0" style="position:absolute">
  <defs>
    <symbol id="i-phone" viewBox="0 0 10 10"><path d="M2 0.8l1.6 2-0.9 1.1c0.6 1.2 1.3 1.9 2.4 2.4l1.1-0.9 2 1.6-0.9 1.8C4.6 8.6 1.4 5.4 0.2 1.7z"/></symbol>
    <symbol id="i-mobile" viewBox="0 0 10 10"><rect x="2.5" y="0.7" width="5" height="8.6" rx="0.6" stroke-width="1.1"/></symbol>
    <symbol id="i-mail" viewBox="0 0 10 10"><path d="M0.5 2.5h9v5.5h-9z M0.5 2.5l4.5 3 4.5-3" /></symbol>
    <symbol id="i-globe" viewBox="0 0 10 10"><circle cx="5" cy="5" r="4.5"/></symbol>
  </defs>
</svg>

<!-- Letterhead -->
<section class="sheet letterhead">
  <div class="brand"><span class="brand-square"></span>Kestrel Home Care</div>
  <div class="contact">
    <div>412 Larkspur Row</div>
    <div>Fairbanks, Alaska 34512</div>
    <div class="gap"></div>
    <div class="contact-row"><svg class="icon" width="6" height="6"><use href="#i-phone"/></svg>555-301-4420</div>
    <div class="contact-row"><svg class="icon icon-outline" width="6" height="6"><use href="#i-mobile"/></svg>555-302-7719</div>
    <div class="contact-row"><svg class="icon" width="6" height="6"><use href="#i-mail"/></svg>info@kestrelhomecare.com</div>
  </div>

  <div class="letter-body">
    <div class="greeting">Dear Mr. Reyes,</div>
    <p>Lorem ipsum dolor sit amet, consectetur adipiscing elit. Donec orci purus, luctus vitae dignissim eu, iaculis sed purus. Vivamus faucibus, ipsum nec aliquet viverra, leo mauris condimentum ligula, sit amet sagittis enim ligula quis arcu. Nam egestas tortor id nisi porttitor mattis. In tortor ante, ultricies in suscipit a, tempus non massa. Vivamus et auctor mi. Fusce vel massa nulla. Phasellus nec eros mauris, et scelerisque orci.</p>
    <p>Donec malesuada orci vitae nulla accumsan porta a id massa. Quisque accumsan iaculis magna sit amet fringilla. Maecenas consequat, magna eget tincidunt semper, odio nibh rutrum mi, id feugiat ante nisi eu risus. Vestibulum nunc orci, rhoncus a placerat in, ultricies in mi. Cras mattis varius eros, vel fringilla nisi suscipit eget. Quisque scelerisque sagittis nulla at porttitor.</p>
    <p>Sed id augue vitae urna euismod commodo aliquet a quam. Pellentesque arcu velit, cursus et malesuada ut, consequat et diam. Nullam erat sem, rhoncus id ullamcorper vitae, rhoncus et arcu. In ultricies ultricies nulla, ut rutrum nisi iaculis at. Donec eu magna a metus ornare faucibus. Fusce aliquet faucibus ultricies. Morbi semper, est id tincidunt gravida, sem arcu adipiscing lacus, ac bibendum nulla leo eu purus. Quisque nec diam sed risus consectetur a accumsan quis quis nibh. Vestibulum id purus lorem.</p>
    <p>It is a long established fact that a reader will be distracted by the readable content of a page when looking at its layout. The point of using Lorem Ipsum is that it has a more-or-less normal distribution of letters, as opposed to using 'Content here, content here', making it look like readable English. Many desktop publishing packages</p>
    <p>ada ut, consequat et diam. Nullam erat sem, rhoncus id ullamcorper vitae, rhoncus et arcu. In ultricies ultricies nulla, ut rutrum nisi iaculis at. Donec eu magna a metus ornare faucibus. Fusce aliquet faucibus ultricies. Morbi semper,</p>
    <div class="closing">Sincerely,</div>
    <div class="signature-art" role="img" aria-label="Handwritten signature"></div>
  </div>

  <div class="band">www.kestrelhomecare.com</div>
  <div class="roller-art" role="img" aria-label="Paint roller illustration finishing the red stripe"></div>
</section>

<!-- Business card -->
<section class="sheet card">
  <div class="brand"><span class="brand-square"></span>Kestrel Home Care</div>
  <div class="person">
    <div class="name">Daniel Reyes</div>
    <div class="role">President</div>
  </div>
  <div class="contact">
    <div>412 Larkspur Row</div>
    <div>Fairbanks, Alaska 34512</div>
    <div class="gap"></div>
    <div class="contact-row"><svg class="icon" width="7" height="7"><use href="#i-phone"/></svg>555-301-4420</div>
    <div class="contact-row"><svg class="icon icon-outline" width="7" height="7"><use href="#i-mobile"/></svg>555-302-7719</div>
    <div class="contact-row"><svg class="icon" width="7" height="7"><use href="#i-mail"/></svg>info@kestrelhomecare.com</div>
  </div>
  <div class="band">kestrelhomecare.com</div>
  <div class="roller-art" role="img" aria-label="Paint roller illustration finishing the red stripe"></div>
</section>

<!-- Email signature, wide -->
<section class="sheet sig-wide">
  <div class="brand"><span class="brand-square"></span>Kestrel Home Care</div>
  <div class="divider"></div>
  <div class="contact">
    <div>412 Larkspur Row</div>
    <div>Fairbanks, Alaska 34512</div>
    <div class="gap"></div>
    <div class="contact-row"><svg class="icon" width="7" height="7"><use href="#i-phone"/></svg>555-301-4420</div>
    <div class="contact-row"><svg class="icon icon-outline" width="7" height="7"><use href="#i-mobile"/></svg>555-302-7719</div>
    <div class="contact-row"><svg class="icon" width="7" height="7"><use href="#i-mail"/></svg>info@kestrelhomecare.com</div>
    <div class="contact-row"><svg class="icon" width="7" height="7"><use href="#i-globe"/></svg>www.kestrelhomecare.com</div>
  </div>
  <div class="band"></div>
  <div class="roller-art" role="img" aria-label="Paint roller illustration finishing the red stripe"></div>
</section>

<!-- Email signature, compact -->
<section class="sheet sig-compact">
  <div class="brand"><span class="brand-square"></span>Kestrel Home Care</div>
  <div class="divider one"></div>
  <div class="contact phones">
    <div class="contact-row"><svg class="icon" width="7" height="7"><use href="#i-phone"/></svg>555-301-4420</div>
    <div class="contact-row"><svg class="icon icon-outline" width="7" height="7"><use href="#i-mobile"/></svg>555-302-7719</div>
    <div class="contact-row"><svg class="icon" width="7" height="7"><use href="#i-mail"/></svg>info@kestrelhomecare.com</div>
  </div>
  <div class="divider two"></div>
  <div class="contact address">
    <div>412 Larkspur Row</div>
    <div>Fairbanks, Alaska 34512</div>
    <div>www.kestrelhomecare.com</div>
  </div>
  <div class="band"></div>
  <div class="roller-art" role="img" aria-label="Paint roller illustration finishing the red stripe"></div>
</section>

</body>
</html>
```